Redesign of Gym Rate Card 4 x9

We want to redesign the Gym rate card. We would like a cleaner look like something Quorvel marketing would look like. I am going to upload the .ai files and then a word document with some notes. I am going to provide a link some pictures and logos that you can use, you don't have to use all the pictures, use the ones you feel fit the best. Please don't just copy what we have here. I have given you some notes for guidance, looking for something clean and appealing to a high end clientele.
I DO NOT HAVE THE ABILITY TO READ .AI FILES SO PLEASE SEND ANY SUBMISSIONS IN PDF OR PICTURE FORMAT
Here is the link to photos and logos: https://www.parcelvaultix.net/share/fd/mk3pq7wz0l2bn8vyt5rhea/QTXLpa-r4KhnMuvd82JBEX7?key=bwnr5sla7tzem2hqcdgf0xk41&sp=7ju9dk2q&dl=0
PLEASE READ THE WORD DOCUMENT. IT HAS INSTRUCTIONS ABOUT WHAT I WANT.

```html
<!DOCTYPE html>
<html lang="en">
<head>
<meta charset="utf-8">
<title>Stridewell Personal Training Rack Card</title>
<link rel="stylesheet" href="https://fonts.googleapis.com/css2?family=Montserrat:wght@400;500;600;700;800&display=swap">
<style>
  :root {
    --orange: #ef5a24;
    --ink: #3a3a3a;
    --band: #4b4b4d;
    --muted: #6d6d6d;
    --paper: #ffffff;
    --stage: #f1f1f1;
    --photo-a: #7c7f84;
    --photo-b: #c9c6c2;
  }
  * { margin: 0; padding: 0; box-sizing: border-box; }
  html, body { width: 781px; height: 1200px; overflow: hidden; background: var(--stage); }
  body { font-family: "Montserrat", Arial, sans-serif; color: var(--ink); display: flex; justify-content: center; }

  .rack-card {
    width: 534px; height: 1200px; background: var(--paper);
    display: flex; flex-direction: column;
  }

  .brand { flex: 0 0 150px; display: flex; align-items: center; justify-content: center; gap: 12px; }
  .brand-dot { width: 14px; height: 14px; border-radius: 50%; background: var(--orange); }
  .brand-name { font-size: 40px; font-weight: 800; letter-spacing: 2px; color: var(--ink); }

  .hero-photo {
    flex: 0 0 380px;
    background: linear-gradient(160deg, var(--photo-b) 0%, var(--photo-a) 70%, #55585c 100%);
  }

  .headline { background: var(--orange); color: #fff; text-align: center; padding: 12px 0 10px; }
  .headline-main { font-size: 36px; font-weight: 800; letter-spacing: 0.5px; line-height: 1; }
  .headline-sub { font-size: 17px; font-weight: 700; letter-spacing: 2px; margin-top: 4px; }

  .intro { background: var(--band); color: #fff; padding: 14px 26px; font-size: 12px; line-height: 1.55; }

  .benefits { list-style: none; padding: 20px 34px 0; }
  .benefit { display: flex; gap: 16px; margin-bottom: 12px; }
  .benefit-icon { flex: 0 0 28px; width: 28px; height: 28px; margin-top: 2px; }
  .benefit-title { font-size: 13px; font-weight: 700; color: var(--orange); }
  .benefit-text { font-size: 10.5px; line-height: 1.45; color: var(--ink); margin-top: 2px; }

  .site { margin-top: auto; padding-bottom: 38px; text-align: center; font-size: 13px; font-weight: 500; letter-spacing: 4px; color: var(--ink); }
</style>
</head>
<body>
<main class="rack-card">
  <header class="brand">
    <span class="brand-dot"></span>
    <span class="brand-name">STRIDEWELL</span>
  </header>

  <div class="hero-photo" role="img" aria-label="Photo of a trainer coaching a client lifting a weighted ball in the studio"></div>

  <section class="headline">
    <h1 class="headline-main">PERSONAL TRAINING</h1>
    <p class="headline-sub">WITH PURPOSE</p>
  </section>

  <p class="intro">At Stridewell, we don't believe in one-size-fits-all fitness. Every program we create is customized to your body, goals, and lifestyle. Whether you're training for a milestone event, building strength after injury, or reclaiming your health — your journey is our priority.</p>

  <ul class="benefits">
    <li class="benefit">
      <svg class="benefit-icon" viewBox="0 0 40 40" fill="var(--orange)"><rect x="4" y="12" width="6" height="16" rx="1"/><rect x="30" y="12" width="6" height="16" rx="1"/><rect x="10" y="17" width="20" height="6"/><rect x="1" y="16" width="3" height="8"/><rect x="36" y="16" width="3" height="8"/></svg>
      <div><h2 class="benefit-title">Build Strength</h2><p class="benefit-text">We design strength programs that not only develop full-body power but also create a stronger, more balanced you — the foundation for every movement you make.</p></div>
    </li>
    <li class="benefit">
      <svg class="benefit-icon" viewBox="0 0 40 40" fill="none" stroke="var(--orange)" stroke-width="4" stroke-linecap="round"><path d="M6 20h28M12 13l-7 7 7 7M28 13l7 7-7 7"/></svg>
      <div><h2 class="benefit-title">Increase Flexibility</h2><p class="benefit-text">Our training methods blend strength with dynamic control, using mobility and stretching patterns that help improve flexibility, posture, and joint health over time.</p></div>
    </li>
    <li class="benefit">
      <svg class="benefit-icon" viewBox="0 0 40 40" fill="var(--orange)"><rect x="5" y="8" width="30" height="27" rx="3"/><rect x="9" y="16" width="22" height="15" fill="#fff"/><rect x="11" y="4" width="4" height="8" rx="1"/><rect x="25" y="4" width="4" height="8" rx="1"/><rect x="13" y="19" width="5" height="4"/><rect x="22" y="24" width="5" height="4"/></svg>
      <div><h2 class="benefit-title">Train for a Life Event</h2><p class="benefit-text">Whether you're preparing for a wedding, vacation, or milestone birthday — we'll craft a focused training plan to help you look and feel your best on the day.</p></div>
    </li>
    <li class="benefit">
      <svg class="benefit-icon" viewBox="0 0 40 40" fill="var(--orange)"><rect x="4" y="6" width="32" height="30" rx="5"/><circle cx="20" cy="17" r="7" fill="#fff"/><path d="M20 17l4-4" stroke="var(--orange)" stroke-width="2.5"/></svg>
      <div><h2 class="benefit-title">Weight Loss</h2><p class="benefit-text">Our weight loss programs combine intelligent resistance training, cardio and lifestyle guidance to help you reach your goals and keep the results long-term.</p></div>
    </li>
    <li class="benefit">
      <svg class="benefit-icon" viewBox="0 0 40 40" fill="none" stroke="var(--orange)" stroke-width="4" stroke-linecap="round" stroke-linejoin="round"><path d="M5 30l10-10 7 6 13-14"/><path d="M27 12h8v8"/></svg>
      <div><h2 class="benefit-title">Improve Functional Movement</h2><p class="benefit-text">We help you move better and stay stronger as you age — with training that improves balance, joint strength, and your ability to stay active and independent.</p></div>
    </li>
  </ul>

  <p class="site">STRIDEWELLTRAINING.COM</p>
</main>
</body>
</html>
```